Quimby's Yard & Garden Center Business Card Update

I need an updated Business card design for my Lawn and Garden Center. We do Landscaping installs, Lawn Mowing, Snow Removal and also have a Garden Center Retail Division. I uploaded a few of our previous business cards to give an idea of what we are starting with. The main goal of this update is to simplify and modernize the business card, not all of the services that are on the previous cards has to be on the new one but I would still like to highlight our main services. There is also a sample of our logo that Can be used in the design.

Industry/Entity Type

Landscaping

Contact Information for Business Card

Morris Quimby
Morris@Quimbysyardandgarden.example
Business (555) 201-7784
Cell (555) 318-6092

Colors

Designer to choose colors to be used in the design.

Requirements
Must have
• Services Provided :
• Landscaping
• Lawn Maintenance
• Snow Removal
• Garden Center

```html
<!DOCTYPE html>
<html lang="en">
<head>
<meta charset="utf-8">
<title>Quimby's Yard &amp; Garden Center – Business Card</title>
<link rel="stylesheet" href="https://fonts.googleapis.com/css2?family=Montserrat:wght@400;500;600&family=Oswald:wght@400;500&display=swap">
<style>
  :root {
    --canvas-bg: #2b2c2f;
    --card-top: #16457c;
    --card-bottom: #0f2454;
    --leaf-green: #6cc46a;
    --logo-green: #3f7d3a;
    --amber: #e3b074;
    --ink-light: #e6ebf3;
    --divider: rgba(230, 235, 243, 0.7);
  }
  * { box-sizing: border-box; margin: 0; padding: 0; }
  html, body {
    width: 1200px; height: 780px; overflow: hidden;
    background: var(--canvas-bg);
  }
  .sheet {
    width: 1200px; height: 780px;
    display: flex; align-items: center; justify-content: center; gap: 30px;
  }
  .card {
    position: relative;
    width: 570px; height: 326px;
    background: linear-gradient(180deg, var(--card-top) 0%, var(--card-bottom) 100%);
    box-shadow: 0 14px 30px rgba(0,0,0,0.55);
    font-family: "Montserrat", sans-serif;
    color: var(--ink-light);
    overflow: hidden;
  }
  .brand {
    display: flex; align-items: center; gap: 10px;
    color: var(--leaf-green);
    font-family: "Montserrat", sans-serif;
    font-weight: 600;
    white-space: nowrap;
  }
  .brand-dot {
    border-radius: 50%;
    background: var(--logo-green);
    flex: none;
  }
  .card-front .brand {
    position: absolute; left: 50%; top: 50%;
    transform: translate(-50%, -50%);
    font-size: 40px;
  }
  .card-front .brand-dot { width: 36px; height: 36px; }

  .card-back .brand {
    position: absolute; left: 30px; top: 36px;
    font-size: 22px;
  }
  .card-back .brand-dot { width: 20px; height: 20px; }

  .person {
    position: absolute; right: 40px; top: 36px; text-align: right;
  }
  .person-name {
    font-family: "Oswald", sans-serif; font-weight: 400;
    font-size: 28px; letter-spacing: 1px; line-height: 1;
    color: var(--leaf-green); text-transform: uppercase;
    white-space: nowrap;
  }
  .person-title {
    font-size: 11px; letter-spacing: 1.5px; margin-top: 5px;
    text-transform: uppercase;
  }
  .contact {
    position: absolute; left: 20px; right: 20px; top: 132px;
    display: flex; align-items: center; justify-content: center; gap: 14px;
    font-size: 11px; letter-spacing: 0.3px;
    white-space: nowrap;
  }
  .contact-group { display: flex; flex-direction: column; gap: 9px; }
  .contact-phones { align-items: flex-end; }
  .contact-line { display: flex; align-items: center; gap: 8px; }
  .contact-divider { width: 1px; height: 46px; background: var(--divider); }
  .icon {
    width: 18px; height: 18px; border-radius: 4px; flex: none;
    background: #ffffff; display: flex; align-items: center; justify-content: center;
  }
  .icon svg { width: 12px; height: 12px; }
  .company {
    position: absolute; left: 0; right: 0; bottom: 62px; text-align: center;
    font-size: 11px; font-weight: 500; letter-spacing: 1.5px;
    color: var(--amber); text-transform: uppercase;
    white-space: nowrap;
  }
  .services {
    position: absolute; left: 0; right: 0; bottom: 26px; text-align: center;
    font-family: "Oswald", sans-serif; font-weight: 500;
    font-size: 16px; letter-spacing: 0.5px; line-height: 1.2;
    color: var(--leaf-green); text-transform: uppercase;
    white-space: nowrap;
  }
</style>
</head>
<body>
<main class="sheet">
  <section class="card card-front" aria-label="Card front">
    <div class="brand"><span class="brand-dot"></span>Quimby's</div>
  </section>

  <section class="card card-back" aria-label="Card back">
    <div class="brand"><span class="brand-dot"></span>Quimby's</div>

    <div class="person">
      <p class="person-name">Morris Quimby</p>
      <p class="person-title">Founder and CEO</p>
    </div>

    <div class="contact">
      <div class="contact-group contact-phones">
        <div class="contact-line">
          <span>(555) 201-7784</span>
          <span class="icon"><svg viewBox="0 0 12 12"><rect x="1" y="2" width="10" height="8" rx="1" fill="none" stroke="#0f2454" stroke-width="1.4"/><rect x="3" y="4" width="3" height="4" fill="#0f2454"/></svg></span>
        </div>
        <div class="contact-line">
          <span>(555) 318-6092</span>
          <span class="icon"><svg viewBox="0 0 12 12"><rect x="3" y="1" width="6" height="10" rx="1" fill="none" stroke="#0f2454" stroke-width="1.4"/><circle cx="6" cy="9" r="0.7" fill="#0f2454"/></svg></span>
        </div>
      </div>
      <span class="contact-divider"></span>
      <div class="contact-group">
        <div class="contact-line">
          <span class="icon"><svg viewBox="0 0 12 12"><circle cx="6" cy="6" r="4.6" fill="none" stroke="#0f2454" stroke-width="1.2"/><ellipse cx="6" cy="6" rx="2" ry="4.6" fill="none" stroke="#0f2454" stroke-width="1"/><line x1="1.4" y1="6" x2="10.6" y2="6" stroke="#0f2454" stroke-width="1"/></svg></span>
          <span>www.quimbysyardandgarden.example</span>
        </div>
        <div class="contact-line">
          <span class="icon"><svg viewBox="0 0 12 12"><text x="6" y="9.3" text-anchor="middle" font-size="10" font-family="Montserrat, sans-serif" font-weight="600" fill="#0f2454">@</text></svg></span>
          <span>Morris@Quimbysyardandgarden.example</span>
        </div>
      </div>
    </div>

    <p class="company">Quimby's Yard &amp; Garden Center</p>
    <p class="services">Landscaping - Lawn Maintenance - Snow Removal - Garden Center</p>
  </section>
</main>
</body>
</html>
```